依頼詳細
主な参加者は女性になりますので、女性的なデザインでお願いします。バナー制作ですが、ポスターのように縦長サイズのイメージになります。
記載項目
バナーに記載していただきたい内容は以下のとおりです。

---ここから---

2月4日は『妊娠の日』
業界初!マタニティヨガインストラクターと鍼灸師がコラボ!
妊活体操イベント開催

<妊活体操イベント概要>
開催日時:2017年2月4日(土)13:00~14:00
*館内着に着替えるため、余裕をもって30分以上前のご来場をお願いいたします。
開催場所:SPA ORIN(神奈川県横浜市西区南空3-5-7 ソラモールクレオ内)

◆当日のプログラム内容
⑴ご挨拶・趣旨説明
⑵マタニティヨガの話・葉酸の話・にんかツボの話
⑶妊活体操
⑷質疑応答

参加費:3,000円(入館料2,880円を含む)
定員:30名(カップルでのご来場もお待ちしております。)
備考:イベント終了後はSPA ORIN内の施設をご利用いただけます。
(深夜3時以降は別途1,730円の利用料が必要です。)

---ここまで---

妊活体操をイメージできるような画像の使用をお願いいたします。
(後日、こちらで撮影した写真に差し替えを行います。)

なお、イベントの会場はこちらになります。
http://www.spa-orin-web.jp/

イベントの告知・集客はこちらのサイトで行います。
http://mirefolle.com/
サイズ
• 横768px(縦は自由です)
希望イメージ
シンプル 複雑
単色 カラフル
暗い 明るい
日常 高級
遊び心 厳粛
未来的 伝統的
女性的 男性的
希望する色
赤系、茶系、妊活ですのでピンク系を使っていただくようお願いいたします。
納品ファイル
• 高解像度JPG (.jpg)
補足説明
◆コンペ参加条件
・1/16に本イベントに関する撮影を行いますので、イメージ写真の差し替え対応までできる方(今回のコンペ費用に含みます。)
・今後定期的にイベントを開催する方向で検討しておりますので、その際は開催日時や開催場所の修正対応をお願いできる方(こちらは別途2,000円/回の費用をお支払いします。手数料込、税別)
弊社スケジュールの都合により、締切を1/5に変更させていただきます。
ご提案どうぞよろしくお願いいたします。

必要な情報が一番目立つようにレイアウトされており、その他の情報もスッキリと分かりやすく書かれていることで、パソコンでみてもスマホでみても視認性が高かった点を評価させていただきました。女性的な雰囲気もイメージどおりでした。

今回は多数の素敵な提案をいただき感謝しております。どうもありがとうございました。

```html
<!DOCTYPE html>
<html lang="ja">
<head>
<meta charset="utf-8">
<title>妊活体操イベント開催</title>
<link rel="stylesheet" href="https://fonts.googleapis.com/css2?family=M+PLUS+Rounded+1c:wght@500;700;800&family=Noto+Sans+JP:wght@400;500;700&display=swap">
<style>
:root{
  --pink:#e9819a;
  --pink-deep:#e2647f;
  --pink-soft:#f7c9d3;
  --blush:#fdeef1;
  --white:#ffffff;
  --ink:#4b3b3d;
  --ink-soft:#6e5a5d;
}
*{margin:0;padding:0;box-sizing:border-box}
html,body{width:710px;height:1200px;overflow:hidden;background:var(--white)}
body{font-family:"Noto Sans JP",sans-serif;color:var(--ink)}
.banner{position:relative;width:710px;height:1200px;background:var(--blush);overflow:hidden}

.day-band{position:absolute;top:0;left:0;width:710px;height:66px;background:var(--pink);
  display:flex;align-items:center;justify-content:center;color:var(--white);
  font-family:"M PLUS Rounded 1c",sans-serif;font-weight:700;font-size:30px;letter-spacing:2px}

.hero-photo{position:absolute;top:66px;left:0;width:710px;height:480px;
  background:linear-gradient(100deg,#f3dedd 0%,#fbf3f2 35%,#f6e4e2 60%,#fbf5f4 100%)}

.title-panel{position:absolute;top:430px;left:0;width:710px;height:140px}
.title-panel svg{position:absolute;inset:0}

.event-title{position:absolute;top:462px;left:0;width:710px;text-align:center;
  font-family:"M PLUS Rounded 1c",sans-serif;font-weight:800;color:var(--pink-deep);line-height:1.12}
.event-title .line1{display:block;font-size:54px;letter-spacing:4px}
.event-title .line2{display:block;font-size:62px;letter-spacing:3px}

.first-badge{position:absolute;left:52px;top:528px;width:96px;height:96px;border-radius:50%;
  background:var(--pink-deep);color:var(--white);display:flex;align-items:center;justify-content:center;
  font-family:"M PLUS Rounded 1c",sans-serif;font-weight:800;font-size:24px;transform:rotate(-12deg);z-index:3}

.collab-ribbon{position:absolute;left:65px;top:612px;width:580px;height:86px;z-index:2}
.collab-ribbon svg{position:absolute;inset:0}
.collab-ribbon .text{position:absolute;inset:0;display:flex;flex-direction:column;align-items:center;justify-content:center;
  color:var(--white);font-weight:700;font-size:25px;line-height:1.3;padding-left:70px}

.event-date{position:absolute;top:716px;left:0;width:710px;text-align:center;font-weight:700;font-size:34px;color:var(--ink)}
.event-lead{position:absolute;top:772px;left:0;width:710px;text-align:center;font-size:19px;color:var(--ink-soft);white-space:nowrap}

.info-box{position:absolute;top:812px;left:35px;width:640px;background:var(--white);border:2px solid var(--pink-soft);border-radius:6px;padding:8px 24px}
.info-row{display:flex;align-items:center;height:36px;font-size:19px;border-bottom:1px dashed var(--pink-soft);white-space:nowrap}
.info-row:last-child{border-bottom:none}
.info-row dt{width:110px;font-weight:700;color:var(--pink-deep)}
.info-row dt::after{content:"："}
.info-row dd{flex:1}
.info-row .sub{font-size:15px}

.info-note{position:absolute;top:986px;left:35px;width:640px;font-size:15px;color:var(--ink-soft);white-space:nowrap}

.perks{position:absolute;top:1028px;left:25px;width:660px;display:flex;gap:16px}
.perk{display:flex;align-items:center;gap:12px}
.perk-first{flex:0 0 290px}
.perk-second{flex:1}
.perk-mark{flex:none;width:72px;height:72px;border-radius:50%;background:var(--pink);color:var(--white);
  display:flex;flex-direction:column;align-items:center;justify-content:center;font-family:"M PLUS Rounded 1c",sans-serif;font-weight:700;line-height:1}
.perk-mark .label{font-size:12px}
.perk-mark .num{font-size:28px;margin-top:3px}
.perk-text{font-size:16px;font-weight:500;line-height:1.55;white-space:nowrap}
.perk-text em{font-style:normal;color:var(--pink-deep);font-weight:700}

.footnote{position:absolute;top:1150px;left:25px;width:660px;font-size:13px;color:var(--ink-soft);line-height:1.5;white-space:nowrap}
</style>
</head>
<body>
<div class="banner">
  <header class="day-band">2月4日は『妊娠の日』</header>

  <div class="hero-photo" role="img" aria-label="ヨガウェアの女性たちが合掌ポーズで妊活体操をしている写真"></div>

  <div class="title-panel">
    <svg width="710" height="140" viewBox="0 0 710 140" aria-hidden="true">
      <path d="M0 60 Q180 0 355 20 Q540 40 710 0 L710 140 L0 140 Z" fill="var(--blush)"/>
    </svg>
  </div>

  <h1 class="event-title"><span class="line1">妊活体操</span><span class="line2">イベント開催</span></h1>

  <div class="first-badge">業界初!</div>
  <div class="collab-ribbon">
    <svg width="580" height="86" viewBox="0 0 580 86" aria-hidden="true">
      <path d="M0 8 L580 8 L560 43 L580 78 L0 78 L20 43 Z" fill="var(--pink)"/>
    </svg>
    <div class="text"><span>マタニティヨガインストラクターと</span><span>鍼灸師がコラボ!</span></div>
  </div>

  <p class="event-date">2017年2月4日(土) 13:00～14:00</p>
  <p class="event-lead">妊活体操の他、妊娠しやすいカラダづくりや、にんかツボの話も聞けちゃう♪</p>

  <dl class="info-box">
    <div class="info-row"><dt>開催場所</dt><dd>SPA ORIN（スパオリン）</dd></div>
    <div class="info-row"><dt>住　　所</dt><dd>神奈川県横浜市西区南空3-5-7 ソラモールクレオ内</dd></div>
    <div class="info-row"><dt>参 加 費</dt><dd>3,000円</dd></div>
    <div class="info-row"><dt>定　　員</dt><dd>30名 <span class="sub">(ご夫婦やお友達とのご参加もお待ちしております)</span></dd></div>
  </dl>

  <p class="info-note">＊館内着に着替えるため、余裕をもって30分以上前のご来場をお願いいたします。</p>

  <div class="perks">
    <div class="perk perk-first">
      <div class="perk-mark"><span class="label">参加特典</span><span class="num">1</span></div>
      <p class="perk-text">定価<em>6,140円</em>の<br>妊活サプリをプレゼント!</p>
    </div>
    <div class="perk perk-second">
      <div class="perk-mark"><span class="label">参加特典</span><span class="num">2</span></div>
      <p class="perk-text">イベント終了後は、SPA ORIN内の<br>施設を<em>無料</em>でご利用いただけます!</p>
    </div>
  </div>

  <p class="footnote">※入館料2,880円が無料になります。ただし深夜3時以降は別途1,730円の深夜料金が必要です。</p>
</div>
</body>
</html>
```